K7R Business Cards

Business Cards

Contact Information for Business Card

Company name, owner name, license #s, phone & email

Requirements
Should not have
• mailing address

```html
<!DOCTYPE html>
<html lang="en">
<head>
<meta charset="utf-8">
<title>K7R Construction – Business Cards</title>
<link href="https://fonts.googleapis.com/css2?family=Montserrat:ital,wght@0,400;0,500;0,700;0,800;1,400;1,700&display=swap" rel="stylesheet">
<style>
  :root {
    --brand-blue: #213d8c;
    --accent-red: #c8201f;
    --ink: #1f1f24;
    --paper: #ffffff;
    --backdrop: #1b1b1e;
  }
  * { margin: 0; padding: 0; box-sizing: border-box; }
  html, body {
    width: 1200px; height: 900px; overflow: hidden;
    background: var(--backdrop);
    font-family: "Montserrat", Arial, sans-serif;
  }
  .card-sheet {
    position: relative; width: 1200px; height: 900px;
  }
  .card {
    position: absolute; top: 295px;
    width: 540px; height: 309px;
    overflow: hidden;
  }
  .card--front { left: 40px; background: var(--paper); }
  .card--back { left: 620px; background: var(--brand-blue); }

  /* front */
  .company-name {
    position: absolute; left: 28px; top: 30px;
    color: var(--brand-blue); font-weight: 800;
    font-size: 26px; line-height: 1.05; letter-spacing: 1px;
  }
  .company-name span { display: block; font-size: 15px; letter-spacing: 2.5px; }
  .agent-name {
    position: absolute; left: 28px; top: 112px;
    color: var(--brand-blue); font-weight: 700; font-size: 20px;
  }
  .agent-title {
    position: absolute; left: 28px; top: 138px;
    color: var(--ink); font-style: italic; font-size: 12px;
  }
  .agent-rule {
    position: absolute; left: 24px; top: 158px;
    width: 300px; height: 1.5px; background: var(--brand-blue);
  }
  .contact-list {
    position: absolute; left: 28px; top: 170px;
    list-style: none; color: var(--ink); font-size: 12px;
  }
  .contact-list li { display: flex; align-items: center; gap: 8px; height: 20px; }
  .contact-list svg { width: 11px; height: 11px; fill: var(--accent-red); }
  .portrait {
    position: absolute; left: 290px; top: 70px;
    width: 230px; height: 180px;
    background: linear-gradient(180deg, #ffffff 0%, #e9e6e3 45%, #2c2c33 100%);
  }
  .license-band {
    position: absolute; left: 0; top: 240px; width: 540px; height: 26px;
  }
  .license-text {
    position: absolute; right: 28px; top: 245px;
    color: var(--paper); font-size: 12px; font-weight: 500; letter-spacing: .3px;
  }
  .card-edge {
    position: absolute; left: 0; bottom: 0; width: 100%; height: 4px;
    background: var(--brand-blue);
  }

  /* back */
  .back-name {
    position: absolute; inset: 0;
    display: flex; flex-direction: column; align-items: center; justify-content: center;
    color: var(--paper); font-weight: 800;
    font-size: 72px; line-height: 1; letter-spacing: 4px;
  }
  .back-name span { font-size: 30px; letter-spacing: 6px; margin-top: 6px; }
</style>
</head>
<body>
  <main class="card-sheet">
    <section class="card card--front" aria-label="Business card front">
      <div class="company-name">K7R<span>CONSTRUCTION</span></div>

      <h1 class="agent-name">Dana Whitfield</h1>
      <p class="agent-title">Real Estate Agent</p>
      <div class="agent-rule"></div>

      <ul class="contact-list">
        <li>
          <svg viewBox="0 0 24 24" aria-hidden="true"><path d="M6.6 10.8a15.1 15.1 0 0 0 6.6 6.6l2.2-2.2a1 1 0 0 1 1-.25 11.4 11.4 0 0 0 3.6.57 1 1 0 0 1 1 1V20a1 1 0 0 1-1 1A17 17 0 0 1 3 4a1 1 0 0 1 1-1h3.5a1 1 0 0 1 1 1c0 1.25.2 2.45.57 3.6a1 1 0 0 1-.25 1z"/></svg>
          555-014-2273
        </li>
        <li>
          <svg viewBox="0 0 24 24" aria-hidden="true"><path d="M2 5h20v2l-10 6L2 7zm0 4.3 10 6 10-6V19H2z"/></svg>
          dwhitfield@mailbox.com
        </li>
      </ul>

      <div class="portrait" role="img" aria-label="Portrait photo of the agent in a dark suit and tie"></div>

      <svg class="license-band" viewBox="0 0 540 26" aria-hidden="true">
        <polygon points="262,0 540,0 540,26 272,26" fill="var(--brand-blue)"/>
        <line x1="0" y1="0" x2="262" y2="0" stroke="var(--brand-blue)" stroke-width="1.5"/>
      </svg>
      <p class="license-text">MN License #QX418206</p>

      <div class="card-edge"></div>
    </section>

    <section class="card card--back" aria-label="Business card back">
      <div class="back-name">K7R<span>CONSTRUCTION</span></div>
    </section>
  </main>
</body>
</html>
```